New Wedding Decor Web Design Project - GUARANTEED PAYMENT

We need to have a business website for a brand new wedding decor & events company, Lirovelle. We have just established our logo and would love to use this logo on the website.

Because this is a new business venture, we do not have too many pictures to post online. It'd be exciting what your creativity can bring us!

Our website is: www.Lirovelle.ca

Target Market(s)

Our clientele demographic is targeted to brides and bridesmaids in their 20-30 years old.

Industry/Entity Type

Wedding

Requirements
Must have
• - Professional, elegant and artistic look
- Modern feeling
- Very catchy flash intro page
- Ability to show Chatterbook posts
Nice to have
• - Easy to navigate, crisp and clean
- Live vocaline messaging or online messaging

I would like to have navigation pages like: Lirovelle Brand, Collections, Features, Contact Us, etc.

Each page I want it to be clean and easy to read. Something like the following website: http://www.pardunetho.com/

We offer:
BACKDROPS
HEAD, CAKE & RECEIVING TABLES DECOR
CHAIRCOVERS
TABLE CLOTHS & OVERLAYS
NAPKINS
CENTREPIECES
CEREMONY SET-UP
CANDELABRA
CRYSTAL GLOBES
LED LIGHTING
CUSTOM DESIGN AISLE RUNNERS
CAKE STANDS
MONEY BOX
CHARGERS
GOBO LIGHTING
Should not have
• - traditional, old style website
- very static (dull)
- too many images or busy layout
- no "standardized" website templates such as: www.brintaq.com/gallery/weddings

```html
<!DOCTYPE html>
<html lang="en">
<head>
<meta charset="utf-8">
<title>Lirovelle – Wedding Events</title>
<link href="https://fonts.googleapis.com/css2?family=Open+Sans:ital,wght@0,400;0,600;1,400&family=Arimo:wght@400;700&display=swap" rel="stylesheet">
<style>
:root{
  --ink-band:#14160f;
  --page:#ffffff;
  --grey-box:#8a8a8a;
  --grey-frame:#dcdcdc;
  --footer:#8c8c8c;
  --footer-line:#a6a6a6;
  --logo-grey:#8b8b8b;
  --pink:#e23f95;
  --white:#ffffff;
  --soft:#eeeeee;
}
*{margin:0;padding:0;box-sizing:border-box}
html,body{width:1200px;height:1031px;overflow:hidden;background:var(--page);font-family:"Open Sans",sans-serif}
.canvas{position:relative;width:1200px;height:1031px}
.top-band{position:absolute;left:0;top:0;width:1200px;height:12px;background:var(--ink-band)}
.brand{position:absolute;left:160px;top:13px;width:270px;height:160px}
.brand-flower{position:absolute;left:10px;top:0;width:110px;height:95px;border-radius:50%;
  background:radial-gradient(circle at 50% 45%,#f7a9d2,#e23f95 60%,#b81d6f)}
.brand-name{position:absolute;left:0;top:88px;font-size:54px;font-weight:400;color:var(--logo-grey);letter-spacing:-1px;line-height:1}
.brand-tag{position:absolute;left:130px;top:138px;font-size:17px;color:var(--logo-grey);letter-spacing:1px}
.live-support{position:absolute;left:793px;top:25px;width:121px;height:29px;background:linear-gradient(#b8b8b8,#8a8a8a);
  border-radius:2px;color:var(--white);font-size:10px;font-weight:600;letter-spacing:.5px;padding:8px 0 0 8px}
.live-support span{position:absolute;right:8px;top:6px;width:22px;height:16px;border-radius:4px;background:#6cbf3e;border:1px solid #3d3d3d}
.social-top{position:absolute;left:920px;top:26px;display:flex;gap:6px}
.social-chip{height:24px;padding:0 5px;border-radius:4px;background:#5b6f9b;color:var(--white);font-size:9px;line-height:24px;font-weight:600}
.social-chip.feed{width:24px;padding:0;background:#f08a1e}
.main-nav{position:absolute;left:457px;top:106px;width:579px;height:65px;background:var(--grey-box);border:1px solid #6a6a6a;
  display:flex;align-items:center;justify-content:space-between;padding:0 12px;color:var(--white);font-size:16px;letter-spacing:.6px}
.main-nav .active{color:#111}
.slider{position:absolute;left:160px;top:177px;width:876px;height:622px;background:var(--grey-frame);border:1px solid #c8c8c8}
.slide{position:absolute;left:13px;top:12px;width:850px;height:598px;
  background:linear-gradient(180deg,#f2c8bc 0%,#d9958a 22%,#1d1a1c 45%,#222 70%,#6b4a24 100%)}
.caption{position:absolute;left:13px;top:555px;width:850px;height:43px;background:rgba(20,20,20,.72);
  color:var(--white);font-family:"Arimo",sans-serif;font-weight:700;font-size:28px;letter-spacing:1px;text-align:center;line-height:43px}
.arrow{position:absolute;top:559px;width:36px;height:36px;border-radius:50%;background:#1a1a1a}
.arrow.prev{left:15px}.arrow.next{left:825px}
.arrow svg{width:36px;height:36px}
.divider-band{position:absolute;left:0;top:799px;width:1200px;height:9px;background:var(--footer)}
.footer{position:absolute;left:0;top:810px;width:1200px;height:221px;background:var(--footer);color:var(--white)}
.footer-flower{position:absolute;left:168px;top:42px;width:112px;height:92px;border-radius:50%;
  background:radial-gradient(circle at 50% 45%,#f7a9d2,#e23f95 60%,#b81d6f)}
.vline{position:absolute;top:60px;width:1px;height:81px;background:var(--footer-line)}
.footer h3{position:absolute;top:40px;font-size:13px;font-weight:600;letter-spacing:.3px}
.offer-list{position:absolute;top:60px;list-style:none;font-size:8.6px;line-height:12.4px;letter-spacing:.5px}
.contact-list{position:absolute;left:643px;top:60px;font-size:8.6px;line-height:12.4px;letter-spacing:.4px}
.contact-list dt{float:left;width:40px}
.social-foot{position:absolute;left:809px;top:61px;display:flex;gap:5px}
.social-foot .social-chip{height:22px;line-height:22px;font-size:8px;padding:0 3px}
.social-foot .feed{width:22px}
.footer-rule{position:absolute;left:162px;top:181px;width:874px;height:1px;background:var(--footer-line)}
.copyright{position:absolute;left:175px;top:196px;font-size:9.5px;font-style:italic}
.footer-nav{position:absolute;right:163px;top:196px;display:flex;gap:19px;font-size:11px;color:#c4c4c4;letter-spacing:.4px}
</style>
</head>
<body>
<div class="canvas">
  <div class="top-band"></div>

  <header>
    <div class="brand">
      <div class="brand-flower" role="img" aria-label="Pink peony flower illustration"></div>
      <div class="brand-name">Lirovelle</div>
      <div class="brand-tag">wedding events</div>
    </div>
    <div class="live-support">LIVE SUPPORT<span></span></div>
    <div class="social-top">
      <div class="social-chip">Chatterbook</div>
      <div class="social-chip">Linkora</div>
      <div class="social-chip">Twitly</div>
      <div class="social-chip feed"></div>
    </div>
    <nav class="main-nav">
      <span class="active">Home</span><span>|</span><span>Gallery</span><span>|</span><span>Lirovelle Brand</span><span>|</span><span>Collection</span><span>|</span><span>Feature</span><span>|</span><span>Contact</span>
    </nav>
  </header>

  <section class="slider">
    <div class="slide" role="img" aria-label="Banquet hall with black tablecloths, black chair covers with red sashes and tall floral centrepieces"></div>
    <div class="caption">Most Beautiful Events...</div>
    <div class="arrow prev"><svg viewBox="0 0 36 36"><path d="M21 9 L12 18 L21 27" fill="none" stroke="#fff" stroke-width="3.5" stroke-linecap="round"/></svg></div>
    <div class="arrow next"><svg viewBox="0 0 36 36"><path d="M15 9 L24 18 L15 27" fill="none" stroke="#fff" stroke-width="3.5" stroke-linecap="round"/></svg></div>
  </section>

  <div class="divider-band"></div>

  <footer class="footer">
    <div class="footer-flower" role="img" aria-label="Pink peony flower illustration"></div>
    <div class="vline" style="left:303px"></div>
    <h3 style="left:318px">We Offer:</h3>
    <ul class="offer-list" style="left:317px">
      <li>BACKDROPS</li><li>HEAD, CAKE &amp;</li><li>CHAIRCOVERS</li><li>TABLE CLOTHS</li><li>NAPKINS</li><li>CENTREPIECES</li>
    </ul>
    <ul class="offer-list" style="left:425px;top:66px">
      <li>CANDELABRA</li><li>CRYSTAL GLOBES</li><li>LED LIGHTING</li><li>CUSTOM DESIGN</li><li>CAKE STANDS</li><li>MONEY BOX</li>
    </ul>
    <ul class="offer-list" style="left:539px;top:65px">
      <li>GOBO LIGHTING</li><li>CHARGERS</li>
    </ul>
    <div class="vline" style="left:634px"></div>
    <h3 style="left:641px">Contact us</h3>
    <dl class="contact-list">
      <dt>Call</dt><dd>(+900) 555-010-020</dd>
      <dt>Email</dt><dd>hello@lirovelle.ca</dd>
      <dt>Vocaline</dt><dd>lirovelle001</dd>
    </dl>
    <div class="vline" style="left:795px"></div>
    <h3 style="left:811px">Follow Us</h3>
    <div class="social-foot">
      <div class="social-chip">Chatterbook</div>
      <div class="social-chip">Linkora</div>
      <div class="social-chip">Twitly</div>
      <div class="social-chip feed"></div>
    </div>
    <div class="footer-rule"></div>
    <div class="copyright">Copyright@Lirovelle.Com</div>
    <nav class="footer-nav">
      <span>Home</span><span>Gallery</span><span>Lirovelle Brand</span><span>Collection</span><span>Features</span><span>Contact Us</span>
    </nav>
  </footer>
</div>
</body>
</html>
```